Business Process / Lifecycle Diagram for Consulting Firm

We are a Delaware-based business modernization and transition-readiness firm. We need a clean, professional process diagram that visually represents our client lifecycle. This is not a marketing funnel or sales graphic — it is a product and delivery lifecycle.

The diagram must be reusable across pitch decks, one-pagers, grant applications, and our website.

Required Structure (must follow exactly)
Stage 1 — Diagnose
Enterprise Upgrade Audit (EUA)
Shift Preparedness Gauge™ (SPG)
(Parallel entry points, equal visual weight)

→ Output: Diagnostic Insight & Priority Signals

Stage 2 — Clarify
Modernization Roadmap (Co-Created)

Stage 3 — Modernize
Q7 — Margin & Momentum Track

Stage 4 — Sustain
Ongoing Modernization Support

Foundation Layer (supports all stages)
HRG-OS™ pillars: People, Process, Systems, Insight

End Outcome
- Operational Clarity
- Sustainable Profitability
- Long-Term Stability

Design Requirements
- Professional, calm (not startup / SaaS style)
- Minimal text, clear hierarchy
- Horizontal or left-to-right flow preferred
- No funnels, no sales language, no aggressive arrows
- Must be delivered as editable vector (AI, SVG, or Figma)

Brand Notes
- Neutral color palette that complements logo attached (Gold Color Code C39E11, Navy Blue code 002C55)
- One accent color for emphasis
- Clean typography
- Should feel credible to business owners, advisors, and lenders
- See website (https://www.hazelmereridgegroup.com/) and LinkedIn (https://www.hazelmereridgegroup.com/) for additional insight into branding.

What NOT to Do
- Do not rename stages
- Do not combine stages
- Do not add extra steps

```html
<!DOCTYPE html>
<html lang="en">
<head>
<meta charset="utf-8">
<title>Hazelmere Ridge Group — Client Lifecycle</title>
<link href="https://fonts.googleapis.com/css2?family=Open+Sans:wght@400;600;700&display=swap" rel="stylesheet">
<style>
  :root{
    --navy:#002d96;
    --gold:#bf9a08;
    --mist:#ebf3ef;
    --band:#e4efec;
    --white:#ffffff;
  }
  *{box-sizing:border-box;margin:0;padding:0}
  html,body{width:1200px;height:631px;overflow:hidden;background:var(--white)}
  body{font-family:"Open Sans",sans-serif;color:var(--navy);position:relative}
  .brand{position:absolute;left:0;width:1200px;top:72px;text-align:center;
    font-size:30px;font-weight:600;letter-spacing:1px;color:var(--navy)}
  .stage-head{position:absolute;top:209px;width:169px;height:61px;border-radius:4px;
    background:var(--navy);text-align:center;display:flex;flex-direction:column;justify-content:center;line-height:1.15}
  .stage-head .num{color:var(--gold);font-size:16px;font-weight:400}
  .stage-head .name{color:var(--white);font-size:17px;font-weight:700;letter-spacing:.3px}
  .stage-head.accent{background:var(--gold)}
  .stage-head.accent .num{color:var(--white)}
  .card{position:absolute;border:1px solid var(--navy);background:var(--mist);
    display:flex;align-items:center;justify-content:center;text-align:center;
    font-size:15px;line-height:1.2}
  .card.tall{top:284px;height:177px;width:169px;align-items:flex-start;padding-top:54px}
  .card.accent{border-color:var(--gold);background:var(--white)}
  .entry{left:59px;width:169px;height:83px;font-size:14px;line-height:1.05}
  .insight{position:absolute;left:278px;top:311px;width:117px;height:123px;border-radius:8px;
    background:var(--gold);color:var(--white);font-weight:700;font-size:13.5px;line-height:1.25;
    display:flex;align-items:center;justify-content:center;text-align:center}
  .links{position:absolute;left:0;top:0}
  .outcome{position:absolute;left:1023px;top:271px;width:145px}
  .outcome h2{color:var(--gold);font-size:21px;font-weight:700;padding-bottom:4px;border-bottom:2px solid var(--gold)}
  .outcome ul{list-style:none}
  .outcome li{position:absolute;left:14px;font-size:17.5px;line-height:1.15;width:140px}
  .outcome li::before{content:"";position:absolute;left:-11px;top:8px;width:7px;height:7px;border-radius:50%;background:var(--gold)}
  .foundation{position:absolute;left:59px;top:484px;width:934px;height:87px;border-radius:9px;overflow:hidden;background:var(--band)}
  .foundation h3{height:36px;background:var(--navy);color:var(--white);font-weight:400;font-size:21px;text-align:center;line-height:36px}
  .pillars{display:flex;height:51px;align-items:center}
  .pillar{flex:1;display:flex;align-items:center;justify-content:center;gap:6px;font-size:19.5px;border-right:2px solid var(--navy);height:28px}
  .pillar:last-child{border-right:none}
  .pillar svg{width:24px;height:24px}
</style>
</head>
<body>
  <div class="brand">Hazelmere Ridge Group</div>

  <div class="stage-head" style="left:59px"><span class="num">Stage 1</span><span class="name">DIAGNOSE</span></div>
  <div class="stage-head" style="left:425px"><span class="num">Stage 2</span><span class="name">CLARIFY</span></div>
  <div class="stage-head accent" style="left:614px"><span class="num">Stage 3</span><span class="name">MODERNIZE</span></div>
  <div class="stage-head" style="left:803px"><span class="num">Stage 4</span><span class="name">SUSTAIN</span></div>

  <div class="card entry" style="top:284px">Enterprise<br>Upgrade<br>Audit (EUA)</div>
  <div class="card entry" style="top:378px">Shift<br>Preparedness<br>Gauge™ (SPG)</div>

  <svg class="links" width="1200" height="631" aria-hidden="true">
    <g fill="none" stroke="#002d96" stroke-width="0.8">
      <path d="M228 326H256V419H228"/>
      <path d="M256 372H278"/>
      <path d="M399 372H425"/>
    </g>
    <circle cx="276" cy="372" r="8" fill="#bf9a08"/>
    <circle cx="397" cy="372" r="8" fill="#bf9a08"/>
  </svg>

  <div class="insight">Diagnostic<br>Insight<br>&amp; Priority<br>Signals</div>

  <div class="card tall" style="left:425px">Modernization<br>Roadmap<br>(Co-Created)</div>
  <div class="card tall accent" style="left:614px">Q7 — Margin<br>&amp; Momentum<br>Track</div>
  <div class="card tall" style="left:803px;padding-top:50px">Ongoing<br>Modernization<br>Support</div>

  <section class="outcome">
    <h2>End Outcome</h2>
    <ul>
      <li style="top:42px">Operational Clarity</li>
      <li style="top:106px">Sustainable Profitability</li>
      <li style="top:165px">Long-Term Stability</li>
    </ul>
  </section>

  <section class="foundation">
    <h3>HRG-OS™ pillars</h3>
    <div class="pillars">
      <div class="pillar">
        <svg viewBox="0 0 24 24" fill="none" stroke="#002d96" stroke-width="1.3"><circle cx="12" cy="6" r="3" stroke="#bf9a08"/><circle cx="7" cy="13" r="2.5"/><circle cx="17" cy="13" r="2.5"/><path d="M2 22c0-3 2-5 5-5s5 2 5 5M12 22c0-3 2-5 5-5s5 2 5 5"/></svg>People</div>
      <div class="pillar">
        <svg viewBox="0 0 24 24" fill="none" stroke="#002d96" stroke-width="1.3"><rect x="3" y="2" width="18" height="20"/><path d="M6 7h12M6 12h12M6 17h12"/><circle cx="10" cy="7" r="1.5" fill="#bf9a08" stroke="none"/><circle cx="14" cy="12" r="1.5" fill="#bf9a08" stroke="none"/><circle cx="9" cy="17" r="1.5" fill="#bf9a08" stroke="none"/></svg>Process</div>
      <div class="pillar">
        <svg viewBox="0 0 24 24" fill="none" stroke-width="1.4"><circle cx="8" cy="8" r="4" stroke="#002d96" stroke-dasharray="2 1.2"/><circle cx="16" cy="16" r="5" stroke="#bf9a08" stroke-dasharray="2.4 1.3"/><circle cx="16" cy="16" r="2" stroke="#bf9a08"/></svg>Systems</div>
      <div class="pillar">
        <svg viewBox="0 0 24 24" fill="none" stroke-width="1.4"><path d="M3 3v18h18" stroke="#002d96"/><path d="M6 17l6-5 3 2 5-8M16 5h4v4" stroke="#bf9a08"/></svg>Insight</div>
    </div>
  </section>
</body>
</html>
```